TopQuizLane needs a dashboard page designed

Redesign the dashboard shown in the provided images.

There are two images:

NOTE: The vocabulary navigation on the left will be a very long list of words 100s, so keep that in mind when you're designing both the vocab navigation and the expanded vocab popup.

In the dashboard.png picture, there needs to be a progress chart showing the word progress like the following: review 1(show it as completed) -> review 2(show the user they are here) -> review 3(unvisited) -> review 4(unvisited)

The do-not-design-this-page.png image is for your reference only. It is not to be designed. Use it to understand the overall look and feel of the website to help you create the best dashboard page possible.
Updates

Need extra days to review

Industry/Entity Type

Education English learning

Number of Pages Required

1 page

Requirements
Must have
• The main navigation and main header cannot change between pages. See the do-not-design page for the main navigateion and header.
Should not have
• Do not add a person profile. We will not have images of our users. Keep the icons in the main navigation as they are.

```html
<!DOCTYPE html>
<html lang="en">
<head>
<meta charset="utf-8">
<title>TopQuizLane – Vocabulary Dashboard</title>
<link href="https://fonts.googleapis.com/css2?family=Plus+Jakarta+Sans:wght@400;500;600;700&display=swap" rel="stylesheet">
<style>
:root{
  --page:#ababab;
  --dark:#262a33;
  --rail:#2a2f38;
  --white:#ffffff;
  --main-bg:#f6f7f9;
  --line:#e6e8ec;
  --ink:#1d2026;
  --muted:#5d626b;
  --faint:#a6abb3;
  --blue:#2f66b8;
  --link:#2f66d0;
  --select:#e9f1fd;
  --purple:#6a4cf0;
  --orange:#ffa62b;
  --sky:#1f8ae0;
  --red:#ee2f5e;
  --gold:#f2b705;
}
*{box-sizing:border-box;margin:0;padding:0}
html,body{width:933px;height:1200px;overflow:hidden;background:var(--page)}
body{font-family:"Plus Jakarta Sans",sans-serif;color:var(--ink)}
.stage{width:1540px;height:1981px;transform:scale(.6058);transform-origin:0 0;position:relative;background:var(--page)}
.screen{position:absolute;left:50px;width:1440px;height:915px;background:var(--main-bg);overflow:hidden}
.screen.one{top:50px}
.screen.two{top:1016px}
.abs{position:absolute}

/* header */
.topbar{left:0;top:0;width:1440px;height:53px;background:var(--dark);color:#fff}
.brand-mark{left:23px;top:14px;width:32px;height:32px;border-radius:9px;background:linear-gradient(135deg,#4f8ff7,#2a5bd7)}
.brand-name{left:110px;top:14px;font-size:21px;font-weight:700;letter-spacing:-.2px}
.tour{left:696px;top:17px;font-size:16px;font-weight:500;display:flex;gap:12px;align-items:center}
.round-btn{top:11px;width:33px;height:33px;border-radius:50%;border:1px solid #4a505b;display:flex;align-items:center;justify-content:center}
.avatar{border-radius:50%;background:linear-gradient(160deg,#e8e2dc,#a58a76)}
.online{left:1396px;top:32px;width:12px;height:12px;border-radius:50%;background:#27c25a;border:2px solid var(--dark)}

/* rail */
.rail{left:0;top:53px;width:78px;height:862px;background:var(--rail)}
.home{left:15px;top:25px;width:48px;height:48px;border-radius:50%;background:#fff;display:flex;align-items:center;justify-content:center}
.rail-icon{left:27px;width:24px;height:24px}

/* word list */
.wordlist{left:78px;top:53px;width:288px;height:862px;background:var(--white);border-right:1px solid var(--line)}
.filter{left:16px;top:22px;font-size:16px;font-weight:600;display:flex;gap:14px;align-items:center}
.expand{right:16px;top:22px;font-size:16px;font-weight:600;color:var(--link)}
.group{position:absolute;left:0;width:288px;height:56px;padding:0 24px;display:flex;align-items:center;justify-content:space-between;font-size:18px;font-weight:600;border-bottom:1px solid var(--line)}
.word{position:absolute;left:0;width:288px;height:44px;padding-left:24px;display:flex;align-items:center;font-size:14px;color:var(--muted);border-bottom:1px solid var(--line)}
.word.active{height:54px;background:var(--select);color:var(--ink);font-size:16px;font-weight:500;border-left:4px solid var(--blue);padding-left:20px}

/* progress */
.step{top:78px;height:57px;width:247px;padding:9px 16px;background:#fff;clip-path:polygon(0 0,93% 0,100% 50%,93% 100%,0 100%,4% 50%)}
.step.first{background:var(--blue);color:#fff;clip-path:polygon(0 0,94% 0,100% 50%,94% 100%,0 100%)}
.step-title{font-size:15px;font-weight:500}
.step-sub{font-size:12px;color:var(--muted);margin-top:3px}
.step.first .step-sub{color:#dfe8f7}
.step.todo .step-title{color:var(--faint)}
.step.todo .step-sub{color:var(--faint)}
.step-star{position:absolute;right:24px;top:9px;width:39px;height:39px;border-radius:50%;display:flex;align-items:center;justify-content:center}

/* word detail */
.word-title{left:398px;top:178px;font-size:26px;font-weight:700;display:flex;gap:12px;align-items:center}
.cta{left:1066px;top:169px;width:342px;height:48px;border-radius:24px;background:var(--dark);color:#fff;display:flex;align-items:center;justify-content:center;gap:12px;font-size:16px;font-weight:600}
.definition{left:398px;top:252px;width:1000px;font-size:14px;line-height:24px;color:var(--muted)}

/* chart card */
.chart-card{left:398px;top:347px;width:1009px;height:389px;background:#fff;border:1px solid var(--line);border-radius:22px}
.chart-icon{left:23px;top:24px;width:48px;height:48px;border-radius:50%;background:#eef2f8;display:flex;align-items:center;justify-content:center}
.chart-title{left:83px;top:36px;font-size:19px;font-weight:600}
.range{left:635px;top:26px;height:40px;border-radius:20px;background:#f3f4f6;display:flex;align-items:center;padding:0 4px;font-size:14px;font-weight:500}
.range span{padding:8px 12px;color:var(--muted)}
.range .on{background:#fff;border-radius:16px;color:var(--ink);box-shadow:0 1px 3px rgba(0,0,0,.08)}
.legend{left:23px;font-size:14px;font-weight:500}
.gridline{left:260px;width:726px;height:1px;background:#eef0f3}
.bar{position:absolute;width:32px;bottom:58px;border-radius:16px 16px 0 0}
.month{position:absolute;top:343px;width:40px;text-align:center;font-size:12px;color:var(--muted)}

.analysis-title{left:398px;top:776px;font-size:18px;font-weight:600}
.analysis{left:398px;top:816px;width:1000px;font-size:14px;line-height:24px;color:var(--muted)}

/* expanded word picker */
.scrim{left:0;top:0;width:1440px;height:915px;background:rgba(28,33,42,.55)}
.picker{left:527px;top:251px;width:507px;height:412px;background:#fff;border-radius:10px;padding:30px}
.picker-head{display:flex;justify-content:space-between;align-items:center;font-size:16px;font-weight:600;height:30px}
.picker-close{width:29px;height:29px;border-radius:50%;background:#fde4e8;display:flex;align-items:center;justify-content:center}
.picker-group{font-size:15px;font-weight:500;margin-top:22px;margin-bottom:12px}
.chips{display:flex;flex-wrap:wrap;gap:11px 10px}
.chip{height:31px;padding:0 12px;border-radius:4px;background:#f1f2f4;font-size:13px;display:flex;align-items:center;color:var(--ink)}
.chip.active{background:var(--select);color:var(--link)}
</style>
</head>
<body>
<div class="stage">

<!-- Screen one -->
<section class="screen one">
  <header class="topbar abs">
    <div class="brand-mark abs"></div>
    <div class="brand-name abs">TopQuizLane</div>
    <div class="tour abs">WordPath Tour <svg width="14" height="9" viewBox="0 0 14 9"><path d="M1 1l6 6 6-6" stroke="#fff" stroke-width="1.8" fill="none"/></svg></div>
    <div class="round-btn abs" style="left:1290px"><svg width="16" height="16"><path d="M8 2v12M2 8h12" stroke="#cfd3da" stroke-width="1.6"/></svg></div>
    <div class="round-btn abs" style="left:1332px"><svg width="16" height="16"><path d="M4 11V7a4 4 0 018 0v4l1 1H3zM6.5 13.5h3" stroke="#cfd3da" stroke-width="1.4" fill="none"/></svg></div>
    <div class="avatar abs" role="img" aria-label="User profile photo" style="left:1374px;top:10px;width:34px;height:34px"></div>
    <div class="online abs"></div>
  </header>
  <nav class="rail abs">
    <div class="home abs"><svg width="22" height="22" viewBox="0 0 22 22"><path d="M3 10l8-7 8 7v9H3z" stroke="#262a33" stroke-width="2" fill="none" stroke-linejoin="round"/></svg></div>
    <svg class="rail-icon abs" style="top:151px" viewBox="0 0 24 24"><path d="M3 5h7l2 2 2-2h7v14h-7l-2 1-2-1H3z" fill="#59606b"/></svg>
    <svg class="rail-icon abs" style="top:215px" viewBox="0 0 24 24"><path d="M4 21V5h9v16M13 10h7v11M6 8h2M6 12h2M6 16h2M10 8h1M10 12h1M15 14h3M15 17h3" stroke="#59606b" stroke-width="1.8" fill="none"/></svg>
    <svg class="rail-icon abs" style="top:781px" viewBox="0 0 24 24"><circle cx="12" cy="12" r="3.5" stroke="#59606b" stroke-width="1.8" fill="none"/><circle cx="12" cy="12" r="8" stroke="#59606b" stroke-width="1.8" fill="none" stroke-dasharray="4 2.3"/></svg>
    <div class="avatar abs" role="img" aria-label="User profile photo" style="left:15px;top:833px;width:48px;height:48px"></div>
  </nav>
  <aside class="wordlist abs">
    <div class="filter abs">All <svg width="14" height="9" viewBox="0 0 14 9"><path d="M1 1l6 6 6-6" stroke="#1d2026" stroke-width="1.8" fill="none"/></svg></div>
    <div class="expand abs">Expand</div>
    <div class="group" style="top:63px">Short-Term Memory <svg width="18" height="10"><path d="M1 9l8-7 8 7" stroke="#8a8f98" stroke-width="1.6" fill="none"/></svg></div>
    <div class="word active" style="top:119px">Grab</div>
    <div class="group" style="top:173px">Working Memory <svg width="18" height="10"><path d="M1 9l8-7 8 7" stroke="#8a8f98" stroke-width="1.6" fill="none"/></svg></div>
    <div class="word" style="top:229px">Cool Down</div>
    <div class="word" style="top:273px">Crave</div>
    <div class="word" style="top:317px">Go For</div>
    <div class="word" style="top:361px">Go-To</div>
    <div class="word" style="top:405px">In The Mood For</div>
    <div class="word" style="top:449px">Sip</div>
    <div class="word" style="top:493px">Soothing</div>
    <div class="word" style="top:537px">Stick With</div>
    <div class="word" style="top:581px">Throw In/Throw On</div>
    <div class="group" style="top:625px">Long-Term Memory <svg width="18" height="10"><path d="M1 9l8-7 8 7" stroke="#8a8f98" stroke-width="1.6" fill="none"/></svg></div>
    <div class="word" style="top:681px">Give It A Try</div>
  </aside>

  <div class="step first abs" style="left:398px"><div class="step-title">Review 1</div><div class="step-sub">Completed</div>
    <div class="step-star" style="background:#fff"><svg width="18" height="18" viewBox="0 0 24 24"><path d="M12 2l3 7 7 .5-5.5 4.8L18 22l-6-4-6 4 1.5-7.7L2 9.5 9 9z" fill="var(--gold)"/></svg></div></div>
  <div class="step abs" style="left:650px"><div class="step-title" style="padding-left:12px">Review 2</div><div class="step-sub" style="padding-left:12px">In Process</div>
    <div class="step-star" style="background:var(--blue)"><svg width="18" height="18" viewBox="0 0 24 24"><path d="M12 2l3 7 7 .5-5.5 4.8L18 22l-6-4-6 4 1.5-7.7L2 9.5 9 9z" fill="#fff"/></svg></div></div>
  <div class="step todo abs" style="left:902px"><div class="step-title" style="padding-left:12px">Review 3</div><div class="step-sub" style="padding-left:12px">Unvisited</div>
    <div class="step-star" style="background:#f1f2f4"><svg width="18" height="18" viewBox="0 0 24 24"><path d="M12 2l3 7 7 .5-5.5 4.8L18 22l-6-4-6 4 1.5-7.7L2 9.5 9 9z" fill="none" stroke="#a6abb3" stroke-width="1.6"/></svg></div></div>
  <div class="step todo abs" style="left:1155px"><div class="step-title" style="padding-left:12px">Review 4</div><div class="step-sub" style="padding-left:12px">Unvisited</div>
    <div class="step-star" style="background:#f1f2f4"><svg width="18" height="18" viewBox="0 0 24 24"><path d="M12 2l3 7 7 .5-5.5 4.8L18 22l-6-4-6 4 1.5-7.7L2 9.5 9 9z" fill="none" stroke="#a6abb3" stroke-width="1.6"/></svg></div></div>

  <h1 class="word-title abs">Grab <svg width="24" height="24" viewBox="0 0 24 24"><path d="M12 2l3 7 7 .5-5.5 4.8L18 22l-6-4-6 4 1.5-7.7L2 9.5 9 9z" fill="var(--gold)"/></svg></h1>
  <div class="cta abs"><svg width="20" height="20"><circle cx="10" cy="10" r="10" fill="#fff"/><path d="M8 6l6 4-6 4z" fill="#262a33"/></svg>Start Vocabulary Review Exercise 3</div>
  <p class="definition abs">The word "grab" is most commonly used as a verb, meaning to take something quickly or suddenly. Imagine you're running late for school. You don't have time for breakfast, so you quickly grab an apple from the kitchen and rush out the door. As you reach the bus stop, your friend waves and says, "Hey! Let's grab a coffee after class." Later, when you sit down, your phone starts ringing. You grab it from your bag and answer.</p>

  <div class="chart-card abs">
    <div class="chart-icon abs"><svg width="22" height="22" viewBox="0 0 24 24"><path d="M3 21h18M5 21V12l4 3V9l4 3V6l4 3v12M17 13h2" stroke="#2f66d0" stroke-width="1.8" fill="none"/></svg></div>
    <div class="chart-title abs">Learning Curve Graph</div>
    <div class="range abs"><span>1 day</span><span>1 week</span><span>1 month</span><span>1 year</span><span class="on">All Time</span></div>
    <div class="legend abs" style="top:121px;color:var(--orange)">Long-Term Memory</div>
    <div class="legend abs" style="top:172px;color:var(--purple)">Working Memory</div>
    <div class="legend abs" style="top:223px;color:var(--red)">Short-Term Memory</div>
    <div class="legend abs" style="top:274px;color:var(--sky)">Forgotten Memory</div>
    <div class="gridline abs" style="top:128px"></div><div class="gridline abs" style="top:179px"></div><div class="gridline abs" style="top:230px"></div><div class="gridline abs" style="top:281px"></div>
    <div class="bar" style="left:262px;height:152px;background:var(--purple)"></div>
    <div class="bar" style="left:324px;height:202px;background:var(--orange)"></div>
    <div class="bar" style="left:386px;height:49px;background:var(--sky)"></div>
    <div class="bar" style="left:448px;height:99px;background:var(--red)"></div>
    <div class="bar" style="left:510px;height:202px;background:var(--orange)"></div>
    <div class="bar" style="left:572px;height:152px;background:var(--purple)"></div>
    <div class="bar" style="left:634px;height:49px;background:var(--sky)"></div>
    <div class="bar" style="left:696px;height:99px;background:var(--red)"></div>
    <div class="bar" style="left:758px;height:202px;background:var(--orange)"></div>
    <div class="bar" style="left:820px;height:49px;background:var(--sky)"></div>
    <div class="bar" style="left:882px;height:152px;background:var(--purple)"></div>
    <div class="bar" style="left:944px;height:99px;background:var(--red)"></div>
    <div class="month" style="left:258px">Jan</div><div class="month" style="left:320px">Feb</div><div class="month" style="left:382px">Mar</div><div class="month" style="left:444px">Apr</div><div class="month" style="left:506px">May</div><div class="month" style="left:568px">Jun</div><div class="month" style="left:630px">Jul</div><div class="month" style="left:692px">Aug</div><div class="month" style="left:754px">Sep</div><div class="month" style="left:816px">Oct</div><div class="month" style="left:878px">Nov</div><div class="month" style="left:940px">Dec</div>
  </div>

  <h2 class="analysis-title abs">WordPath Tutor Learning Analysis</h2>
  <p class="analysis abs">Lorem ipsum dolor sit amet, consectetur adipiscing elit, sed do eiusmod tempor incididunt ut labore et dolore magna aliqua. Ut enim ad minim veniam, quis nostrud exercitation ullamco laboris nisi ut aliquip ex ea commodo consequat.</p>
</section>

<!-- Screen two: expanded word picker -->
<section class="screen two">
  <header class="topbar abs">
    <div class="brand-mark abs"></div>
    <div class="brand-name abs">TopQuizLane</div>
    <div class="tour abs">WordPath Tour <svg width="14" height="9" viewBox="0 0 14 9"><path d="M1 1l6 6 6-6" stroke="#fff" stroke-width="1.8" fill="none"/></svg></div>
    <div class="round-btn abs" style="left:1290px"><svg width="16" height="16"><path d="M8 2v12M2 8h12" stroke="#cfd3da" stroke-width="1.6"/></svg></div>
    <div class="round-btn abs" style="left:1332px"><svg width="16" height="16"><path d="M4 11V7a4 4 0 018 0v4l1 1H3zM6.5 13.5h3" stroke="#cfd3da" stroke-width="1.4" fill="none"/></svg></div>
    <div class="avatar abs" role="img" aria-label="User profile photo" style="left:1374px;top:10px;width:34px;height:34px"></div>
    <div class="online abs"></div>
  </header>
  <nav class="rail abs">
    <div class="home abs"><svg width="22" height="22" viewBox="0 0 22 22"><path d="M3 10l8-7 8 7v9H3z" stroke="#262a33" stroke-width="2" fill="none" stroke-linejoin="round"/></svg></div>
    <svg class="rail-icon abs" style="top:151px" viewBox="0 0 24 24"><path d="M3 5h7l2 2 2-2h7v14h-7l-2 1-2-1H3z" fill="#59606b"/></svg>
    <svg class="rail-icon abs" style="top:215px" viewBox="0 0 24 24"><path d="M4 21V5h9v16M13 10h7v11M6 8h2M6 12h2M6 16h2M10 8h1M10 12h1M15 14h3M15 17h3" stroke="#59606b" stroke-width="1.8" fill="none"/></svg>
    <svg class="rail-icon abs" style="top:781px" viewBox="0 0 24 24"><circle cx="12" cy="12" r="3.5" stroke="#59606b" stroke-width="1.8" fill="none"/><circle cx="12" cy="12" r="8" stroke="#59606b" stroke-width="1.8" fill="none" stroke-dasharray="4 2.3"/></svg>
    <div class="avatar abs" role="img" aria-label="User profile photo" style="left:15px;top:833px;width:48px;height:48px"></div>
  </nav>
  <aside class="wordlist abs">
    <div class="filter abs">All <svg width="14" height="9" viewBox="0 0 14 9"><path d="M1 1l6 6 6-6" stroke="#1d2026" stroke-width="1.8" fill="none"/></svg></div>
    <div class="expand abs">Expand</div>
    <div class="group" style="top:63px">Short-Term Memory <svg width="18" height="10"><path d="M1 9l8-7 8 7" stroke="#8a8f98" stroke-width="1.6" fill="none"/></svg></div>
    <div class="word active" style="top:119px">Grab</div>
    <div class="group" style="top:173px">Working Memory <svg width="18" height="10"><path d="M1 9l8-7 8 7" stroke="#8a8f98" stroke-width="1.6" fill="none"/></svg></div>
    <div class="word" style="top:229px">Cool Down</div>
    <div class="word" style="top:273px">Crave</div>
    <div class="word" style="top:317px">Go For</div>
    <div class="word" style="top:361px">Go-To</div>
    <div class="word" style="top:405px">In The Mood For</div>
    <div class="word" style="top:449px">Sip</div>
    <div class="word" style="top:493px">Soothing</div>
    <div class="word" style="top:537px">Stick With</div>
    <div class="word" style="top:581px">Throw In/Throw On</div>
    <div class="group" style="top:625px">Long-Term Memory <svg width="18" height="10"><path d="M1 9l8-7 8 7" stroke="#8a8f98" stroke-width="1.6" fill="none"/></svg></div>
    <div class="word" style="top:681px">Give It A Try</div>
  </aside>

  <div class="step first abs" style="left:398px"><div class="step-title">Review 1</div><div class="step-sub">Completed</div>
    <div class="step-star" style="background:#fff"><svg width="18" height="18" viewBox="0 0 24 24"><path d="M12 2l3 7 7 .5-5.5 4.8L18 22l-6-4-6 4 1.5-7.7L2 9.5 9 9z" fill="var(--gold)"/></svg></div></div>
  <div class="step abs" style="left:650px"><div class="step-title" style="padding-left:12px">Review 2</div><div class="step-sub" style="padding-left:12px">In Process</div>
    <div class="step-star" style="background:var(--blue)"><svg width="18" height="18" viewBox="0 0 24 24"><path d="M12 2l3 7 7 .5-5.5 4.8L18 22l-6-4-6 4 1.5-7.7L2 9.5 9 9z" fill="#fff"/></svg></div></div>
  <div class="step todo abs" style="left:902px"><div class="step-title" style="padding-left:12px">Review 3</div><div class="step-sub" style="padding-left:12px">Unvisited</div>
    <div class="step-star" style="background:#f1f2f4"><svg width="18" height="18" viewBox="0 0 24 24"><path d="M12 2l3 7 7 .5-5.5 4.8L18 22l-6-4-6 4 1.5-7.7L2 9.5 9 9z" fill="none" stroke="#a6abb3" stroke-width="1.6"/></svg></div></div>
  <div class="step todo abs" style="left:1155px"><div class="step-title" style="padding-left:12px">Review 4</div><div class="step-sub" style="padding-left:12px">Unvisited</div>
    <div class="step-star" style="background:#f1f2f4"><svg width="18" height="18" viewBox="0 0 24 24"><path d="M12 2l3 7 7 .5-5.5 4.8L18 22l-6-4-6 4 1.5-7.7L2 9.5 9 9z" fill="none" stroke="#a6abb3" stroke-width="1.6"/></svg></div></div>

  <h1 class="word-title abs">Grab <svg width="24" height="24" viewBox="0 0 24 24"><path d="M12 2l3 7 7 .5-5.5 4.8L18 22l-6-4-6 4 1.5-7.7L2 9.5 9 9z" fill="var(--gold)"/></svg></h1>
  <div class="cta abs"><svg width="20" height="20"><circle cx="10" cy="10" r="10" fill="#fff"/><path d="M8 6l6 4-6 4z" fill="#262a33"/></svg>Start Vocabulary Review Exercise 3</div>
  <p class="definition abs">The word "grab" is most commonly used as a verb, meaning to take something quickly or suddenly. Imagine you're running late for school. You don't have time for breakfast, so you quickly grab an apple from the kitchen and rush out the door. As you reach the bus stop, your friend waves and says, "Hey! Let's grab a coffee after class." Later, when you sit down, your phone starts ringing. You grab it from your bag and answer.</p>

  <div class="chart-card abs">
    <div class="chart-icon abs"><svg width="22" height="22" viewBox="0 0 24 24"><path d="M3 21h18M5 21V12l4 3V9l4 3V6l4 3v12M17 13h2" stroke="#2f66d0" stroke-width="1.8" fill="none"/></svg></div>
    <div class="chart-title abs">Learning Curve Graph</div>
    <div class="range abs"><span>1 day</span><span>1 week</span><span>1 month</span><span>1 year</span><span class="on">All Time</span></div>
    <div class="legend abs" style="top:121px;color:var(--orange)">Long-Term Memory</div>
    <div class="legend abs" style="top:172px;color:var(--purple)">Working Memory</div>
    <div class="legend abs" style="top:223px;color:var(--red)">Short-Term Memory</div>
    <div class="legend abs" style="top:274px;color:var(--sky)">Forgotten Memory</div>
    <div class="gridline abs" style="top:128px"></div><div class="gridline abs" style="top:179px"></div><div class="gridline abs" style="top:230px"></div><div class="gridline abs" style="top:281px"></div>
    <div class="bar" style="left:262px;height:152px;background:var(--purple)"></div>
    <div class="bar" style="left:324px;height:202px;background:var(--orange)"></div>
    <div class="bar" style="left:386px;height:49px;background:var(--sky)"></div>
    <div class="bar" style="left:448px;height:99px;background:var(--red)"></div>
    <div class="bar" style="left:510px;height:202px;background:var(--orange)"></div>
    <div class="bar" style="left:572px;height:152px;background:var(--purple)"></div>
    <div class="bar" style="left:634px;height:49px;background:var(--sky)"></div>
    <div class="bar" style="left:696px;height:99px;background:var(--red)"></div>
    <div class="bar" style="left:758px;height:202px;background:var(--orange)"></div>
    <div class="bar" style="left:820px;height:49px;background:var(--sky)"></div>
    <div class="bar" style="left:882px;height:152px;background:var(--purple)"></div>
    <div class="bar" style="left:944px;height:99px;background:var(--red)"></div>
    <div class="month" style="left:258px">Jan</div><div class="month" style="left:320px">Feb</div><div class="month" style="left:382px">Mar</div><div class="month" style="left:444px">Apr</div><div class="month" style="left:506px">May</div><div class="month" style="left:568px">Jun</div><div class="month" style="left:630px">Jul</div><div class="month" style="left:692px">Aug</div><div class="month" style="left:754px">Sep</div><div class="month" style="left:816px">Oct</div><div class="month" style="left:878px">Nov</div><div class="month" style="left:940px">Dec</div>
  </div>

  <h2 class="analysis-title abs">WordPath Tutor Learning Analysis</h2>
  <p class="analysis abs">Lorem ipsum dolor sit amet, consectetur adipiscing elit, sed do eiusmod tempor incididunt ut labore et dolore magna aliqua. Ut enim ad minim veniam, quis nostrud exercitation ullamco laboris nisi ut aliquip ex ea commodo consequat.</p>

  <div class="scrim abs"></div>
  <div class="picker abs" role="dialog" aria-label="All vocabulary words">
    <div class="picker-head"><span style="display:flex;gap:14px;align-items:center">All <svg width="14" height="9" viewBox="0 0 14 9"><path d="M1 1l6 6 6-6" stroke="#1d2026" stroke-width="1.8" fill="none"/></svg></span>
      <span class="picker-close"><svg width="10" height="10"><path d="M1 1l8 8M9 1l-8 8" stroke="#e0334f" stroke-width="1.8"/></svg></span></div>
    <div class="picker-group">Short-Term Memory</div>
    <div class="chips"><span class="chip active">Grab</span></div>
    <div class="picker-group">Short-Term Memory</div>
    <div class="chips"><span class="chip">Cool Down</span><span class="chip">Crave</span><span class="chip">Go For</span><span class="chip">Go-To</span><span class="chip">In The Mood For</span><span class="chip">Sip</span><span class="chip">Soothing</span><span class="chip">Stick With</span><span class="chip">Throw In/Throw On</span></div>
    <div class="picker-group">Long-Term M</div>
    <div class="chips"><span class="chip">Give It A Try</span></div>
  </div>
</section>

</div>
</body>
</html>
```